The Quiet Hour Safeguard Handbook

A book cover. The book will be marketed as a promotional item for financial advisors, financial planners, independent insurance agents, bankers, and any professional who views their role as guardian of their clients assets and helping them manage risk.

```html
<!DOCTYPE html>
<html lang="en">
<head>
<meta charset="utf-8">
<title>The Quiet Hour Safeguard Handbook</title>
<link href="https://fonts.googleapis.com/css2?family=Barlow+Condensed:wght@600;700&family=Inter:wght@300;400;700&display=swap" rel="stylesheet">
<style>
  :root {
    --paper: #f4f1ea;
    --navy-deep: #0b2246;
    --navy: #0f3466;
    --navy-bright: #1d5290;
    --white: #ffffff;
    --gold-1: #f8c62c;
    --gold-2: #fff6cf;
    --gold-3: #c3922f;
    --gold-4: #f6eab8;
  }
  * { margin: 0; padding: 0; box-sizing: border-box; }
  html, body { width: 917px; height: 1200px; overflow: hidden; background: var(--paper); }
  .canvas { position: relative; width: 917px; height: 1200px; background: var(--paper); }
  .cover {
    position: absolute; left: 123px; top: 126px; width: 671px; height: 948px;
    overflow: hidden; background: var(--navy-deep);
  }
  .cover-backdrop {
    position: absolute; inset: 0;
    background:
      radial-gradient(ellipse 70% 30% at 50% 35%, rgba(29,82,144,0.55), transparent 70%),
      radial-gradient(ellipse 80% 25% at 50% 62%, rgba(29,82,144,0.45), transparent 70%),
      linear-gradient(180deg, var(--navy) 0%, var(--navy-deep) 45%, #123a70 65%, var(--navy-deep) 100%);
  }
  .title {
    position: absolute; left: 0; right: 0; top: 42px;
    text-align: center; font-family: "Barlow Condensed", sans-serif; font-weight: 700;
    text-transform: uppercase; color: var(--white); line-height: 1;
  }
  .title-line { display: block; }
  .title-top { font-size: 100px; letter-spacing: -1px; }
  .title-accent {
    font-size: 134px; margin-top: -4px; letter-spacing: -1px;
    background: linear-gradient(90deg, var(--gold-1) 0%, var(--gold-2) 30%, var(--gold-3) 62%, var(--gold-4) 100%);
    -webkit-background-clip: text; background-clip: text; color: transparent;
  }
  .title-bottom { font-size: 92px; margin-top: 2px; letter-spacing: -0.5px; }
  .shield { position: absolute; left: 0; top: 0; width: 671px; height: 948px; }
  .tagline {
    position: absolute; left: 0; right: 0; top: 541px; text-align: center;
    font-family: "Inter", sans-serif; color: var(--white); font-size: 29px; line-height: 35px;
    text-transform: uppercase; font-weight: 300;
  }
  .tagline strong { font-weight: 700; }
  .motto {
    position: absolute; left: 0; right: 0; top: 853px; text-align: center;
    font-family: "Inter", sans-serif; color: var(--white); font-size: 20px; line-height: 26px;
    text-transform: uppercase; font-weight: 300; letter-spacing: -0.2px;
  }
  .motto strong { font-weight: 700; }
</style>
</head>
<body>
<div class="canvas">
  <div class="cover">
    <div class="cover-backdrop" role="img" aria-label="Blue digital city skyline made of glowing data points and numbers"></div>

    <h1 class="title">
      <span class="title-line title-top">The Quiet Hour</span>
      <span class="title-line title-accent">Safeguard</span>
      <span class="title-line title-bottom">Handbook</span>
    </h1>

    <svg class="shield" viewBox="0 0 671 948" aria-hidden="false">
      <defs>
        <linearGradient id="shieldGold" x1="0" y1="0" x2="1" y2="0">
          <stop offset="0" stop-color="#f8c62c"/>
          <stop offset="0.3" stop-color="#fff6cf"/>
          <stop offset="0.62" stop-color="#c3922f"/>
          <stop offset="1" stop-color="#fff6cf"/>
        </linearGradient>
        <linearGradient id="shieldFill" x1="0" y1="0" x2="0" y2="1">
          <stop offset="0" stop-color="#1a4c80"/>
          <stop offset="0.5" stop-color="#0f3463"/>
          <stop offset="1" stop-color="#0a2446"/>
        </linearGradient>
      </defs>
      <path role="img" aria-label="Family of four seen from behind over a faint fingerprint pattern"
            d="M335 390 L142 460 L142 560 C142 680 230 770 335 816 C440 770 528 680 528 560 L528 460 Z"
            fill="url(#shieldFill)"/>
      <path d="M335 390 L142 460 L142 560 C142 680 230 770 335 816 C440 770 528 680 528 560 L528 460 Z"
            fill="none" stroke="url(#shieldGold)" stroke-width="15" stroke-linejoin="miter"/>
    </svg>

    <p class="tagline">
      <strong>Protect yourself</strong><br>
      and your <strong>family</strong><br>
      in the AI age
    </p>

    <p class="motto">
      <strong>It’s better to have it and not need it</strong><br>
      than need it and not have it.
    </p>
  </div>
</div>
</body>
</html>
```